Camp List

Looking to make this camp checklist more appealing and have a camp background. Lettering can me spruced up. The title can me more camp lettering (Driftwood font). Any suggestions?

Target Market(s)

teenagers

Industry/Entity Type

pharmacy

Requirements
Must have
• clean fun organized look
Nice to have
• eye catching
Should not have
• inappropriate pictures or messages

```html
<!DOCTYPE html>
<html lang="en">
<head>
<meta charset="utf-8">
<title>Lindale Pharmacy – Summer Camp List</title>
<link rel="stylesheet" href="https://fonts.googleapis.com/css2?family=Rampart+One&family=Questrial&family=Montserrat:ital,wght@0,600;0,700;1,700&display=swap">
<style>
  :root{
    --page-bg:#e4e4e6;
    --paper:#ffffff;
    --ink:#1d1d1d;
    --contact-bg:#f2895b;
    --pink:#e8228b;
    --orange:#f08a5d;
    --cyan:#9fd8de;
    --green:#cfdf9f;
    --footer-line:#e3e7ad;
    --brand-blue:#2c56b3;
  }
  *{box-sizing:border-box;margin:0;padding:0}
  html,body{width:1200px;height:1200px;overflow:hidden}
  body{background:var(--page-bg);font-family:"Questrial",sans-serif;color:var(--ink);position:relative}
  .flyer{position:absolute;left:240px;top:90px;width:720px;height:1020px;background:var(--paper);box-shadow:0 2px 6px rgba(0,0,0,.25)}
  .brand{position:absolute;left:46px;top:48px;display:flex;align-items:center;gap:10px;
    font-family:"Montserrat",sans-serif;font-weight:700;font-size:28px;color:var(--brand-blue)}
  .brand-mark{width:22px;height:22px;background:var(--brand-blue)}
  .contact{position:absolute;left:414px;top:0;width:306px;height:122px;background:var(--contact-bg);font-style:normal;
    color:#fff;font-family:"Montserrat",sans-serif;font-weight:700;font-size:13px;line-height:18px;padding:32px 0 0 30px}
  .title-art{position:absolute;left:135px;top:132px;width:450px;height:84px;border-radius:10px;
    background:linear-gradient(90deg,#f07fb0,#f9c25a 35%,#9ed6e0 65%,#c7df8a)}
  .tagline{position:absolute;left:0;right:0;top:230px;text-align:center;font-family:"Montserrat",sans-serif;font-weight:700;font-size:16px}
  .box{position:absolute;border:2px solid;border-radius:13px;padding:8px 10px}
  .box h2{font-family:"Rampart One",sans-serif;font-weight:400;font-size:21px;letter-spacing:1px;line-height:26px;margin-bottom:6px;white-space:nowrap}
  .box ul{list-style:none;font-size:13px;line-height:16px}
  .box li{white-space:nowrap}
  .box li::before{content:"• "}
  .cols{display:flex;gap:18px}
  .cols ul{flex:1}
  .pink{border-color:var(--pink)} .pink h2{color:var(--pink)}
  .orange{border-color:var(--orange)} .orange h2{color:var(--orange)}
  .cyan{border-color:var(--cyan)} .cyan h2{color:var(--cyan)}
  .green{border-color:var(--green)} .green h2{color:var(--green)}
  .personal{left:26px;top:277px;width:425px;height:245px}
  .summer{left:460px;top:277px;width:237px;height:115px}
  .otc{left:460px;top:407px;width:237px;height:115px}
  .otc .cols{gap:6px}
  .accessories{left:26px;top:540px;width:184px;height:204px}
  .accessories h2{font-size:19px;letter-spacing:.5px}
  .firstaid{left:221px;top:540px;width:230px;height:182px}
  .hygiene{left:460px;top:540px;width:237px;height:134px}
  .foot{left:26px;top:761px;width:210px;height:126px}
  .swimming{left:249px;top:761px;width:167px;height:156px}
  .gift{position:absolute;left:451px;top:755px;width:249px;text-align:center;font-family:"Rampart One",sans-serif;
    font-size:27px;line-height:34px;letter-spacing:1px}
  .gift .l1,.gift .l2,.gift .l4{color:var(--orange)}
  .gift .l3{color:var(--pink)}
  .gift .amount{font-family:"Questrial",sans-serif;font-size:28px}
  .footer{position:absolute;left:45px;top:945px;width:629px;height:51px;border:2px solid var(--footer-line);border-radius:26px;
    display:flex;align-items:center;justify-content:center;font-family:"Montserrat",sans-serif;font-style:italic;font-weight:700;
    font-size:22px;color:var(--pink)}
</style>
</head>
<body>
<main class="flyer">
  <div class="brand"><span class="brand-mark"></span>Lindale Pharmacy</div>
  <address class="contact">
    88 Orchard Row | Brooklyn, NY 11200<br>
    Tel.: 718-555-0142<br>
    Fax: 718-555-0187<br>
    Email: orders@lindalepharmacy.com
  </address>

  <div class="title-art" role="img" aria-label="Playful multicolour 'Summer Camp' hand lettering with a small sun"></div>
  <p class="tagline">Email your orders for faster service!</p>

  <section class="box pink personal">
    <h2>PERSONAL CARE</h2>
    <div class="cols">
      <ul>
        <li>Spray bottles</li><li>Soap holder</li><li>Toothbrush holder</li><li>Swab tips</li>
        <li>Cosmetic bags</li><li>Mirror</li><li>Comb and brush</li><li>Toothbrush</li>
        <li>Toothpaste</li><li>Dental floss</li><li>StatiCalm®</li><li>Sleep antistatic spray</li>
      </ul>
      <ul>
        <li>Deodorants</li><li>Travel sport gel</li><li>Collapsible travel cup</li><li>Shampoo &amp; Conditioner</li>
        <li>Travel brush</li><li>Mouthwash</li><li>Disposable shavers</li><li>Hair remover (Smoothé®)</li>
        <li>Dermelle® hand cream</li><li>Oativa® moisturizing lotion</li><li>Lipmara chapstick</li><li>Velvaro® lip balm</li>
      </ul>
    </div>
  </section>

  <section class="box orange summer">
    <h2>SUMMER</h2>
    <ul><li>Bite relief</li><li>Bug chaser wrist bands</li><li>Suntan lotions &amp; sprays</li><li>Repellants</li></ul>
  </section>

  <section class="box cyan otc">
    <h2>OTC PRODUCTS</h2>
    <div class="cols">
      <ul><li>Acetril®</li><li>Ibuvex®</li><li>Allerdine®</li></ul>
      <ul><li>Calmodia®</li><li>Chewzac®</li><li>Voyagel®</li></ul>
    </div>
  </section>

  <section class="box green accessories">
    <h2>ACCESSORIES</h2>
    <ul>
      <li>Rain bonnet</li><li>Laundry bags</li><li>Laundry marker</li><li>Batteries</li>
      <li>Flashlight, night light</li><li>LED book light</li><li>Ironlatch®</li><li>Nail clippers</li><li>Scissors</li>
    </ul>
  </section>

  <section class="box orange firstaid">
    <h2>FIRST AID</h2>
    <ul>
      <li>Bandages</li><li>Anti-itch topicals</li><li>Solvira® Spray</li>
      <li>Calamira®, Allerdine®, Cortyx®</li><li>Rubbing alcohol</li><li>Hydrogen peroxide</li><li>Antibiotic cream</li>
    </ul>
  </section>

  <section class="box pink hygiene">
    <h2>HYGIENE</h2>
    <ul><li>Hand sanitizer</li><li>Soap</li><li>Softissa® tissue</li><li>Portable flushable wipes</li></ul>
  </section>

  <section class="box cyan foot">
    <h2>FOOT</h2>
    <ul><li>Shoe polish</li><li>Wax shine</li><li>Shoelaces</li><li>Pedivra® spray &amp; powder</li></ul>
  </section>

  <section class="box green swimming">
    <h2>SWIMMING</h2>
    <ul>
      <li>Goggles (Aquadart®)</li><li>Nose clips</li><li>Ear plugs</li><li>Eye savers</li>
      <li>Swimming caps</li><li>Waterproof earplugs</li>
    </ul>
  </section>

  <p class="gift">
    <span class="l1">FREE GIFT</span><br>
    <span class="l2">WITH</span><br>
    <span class="l3">CAMP ORDERS</span><br>
    <span class="l4">OVER <span class="amount">$30</span></span>
  </p>

  <p class="footer">Wishing you a Happy &amp; Healthy 2023 Summer!</p>
</main>
</body>
</html>
```